Velurana Website Wordpress Template

For the website of the Velurana company, a Wordpress template is to be built for one of the main pages and 3 different landing pages. The design has already been finalized and can be seen in the file 200831_VL_Landingpage. In addition, a location finder is to be installed so that the nearest pharmacy that Velurana sells can be found. The pictures for the slider have already been uploaded. The texts on the main page can be seen in TextVeluranaLandingpageallg.pdf. The texts of the target group landing pages can be seen under TextVeluranaDifferentLandingpage.pdf. An imprint page is to be implemented, but will be filled at a later date.

For the website of the company Velurana a WordPress template for one main page and 3 different landing pages is to be built. The design is already finalized and can be seen in the file 200831_VL_Landingpage. In addition, a store finder should be installed via which the nearest pharmacy, which Velurana distributes, can be found. The images for the sliders are already uploaded. The texts of the main page is described in TextVeluranaLandingpageallg.pdf. The texts of the target group landing pages can be found under TextVeluranaDifferentLandingpage.pdf. An imprint page is to be implemented, but will be filled at a later stage.

```html
<!DOCTYPE html>
<html lang="de">
<head>
<meta charset="utf-8">
<title>Velurana – Schokolade statt Tabletten</title>
<link rel="stylesheet" href="https://fonts.googleapis.com/css2?family=Bree+Serif&display=swap">
<style>
:root{
  --brown:#5a2a27;
  --brown-dark:#4a2523;
  --olive:#5e6434;
  --olive-text:#5a6130;
  --gold:#f4d46c;
  --text:#3b3330;
  --line:#d6d6d6;
  --hero-bg:#f4f4f4;
  --placeholder:#d8d4c2;
  --white:#ffffff;
}
*{margin:0;padding:0;box-sizing:border-box}
html,body{width:1200px;height:2655px;overflow:hidden}
body{position:relative;font-family:"Bree Serif",Georgia,serif;color:var(--text);background:var(--white)}
.abs{position:absolute}

/* hero */
.hero{left:0;top:0;width:1200px;height:682px;background:var(--hero-bg)}
.brand-box{left:111px;top:12px;width:206px;height:206px;background:var(--brown);display:flex;align-items:center;justify-content:center}
.brand-name{color:var(--gold);font-size:31px;letter-spacing:1px}
.tagline{right:112px;text-align:right}
.tagline-1{top:52px;font-size:19px;color:var(--brown)}
.tagline-2{top:84px;font-size:20px;color:var(--olive-text)}
.hero-title{left:111px;top:340px;color:var(--olive-text);line-height:1.15;font-weight:400}
.hero-title .big{font-size:50px;display:block}
.hero-title .small{font-size:42px;display:block;margin-top:6px}
.product{left:570px;top:258px;width:580px;height:400px;background:var(--placeholder)}
.curve{left:0;top:680px}
.dots{left:566px;top:762px;display:flex;gap:5px}
.dot{width:13px;height:13px;border-radius:50%;background:var(--olive)}
.dot.active{background:transparent;border:2px solid var(--olive)}

/* intro */
.intro{left:212px;top:868px;width:776px;text-align:center;font-size:17px;line-height:33.5px;color:var(--text)}

/* finder */
.finder{left:0;top:1124px;width:1200px;height:718px;background:var(--olive)}
.finder-title{left:0;top:1176px;width:1200px;text-align:center;color:var(--white);font-size:30px;font-weight:400}
.finder-btn{left:319px;top:1243px;width:562px;height:57px;border-radius:29px;background:var(--white);display:flex;align-items:center;justify-content:center;font-size:16px;color:var(--text)}
.map-frame{left:165px;top:1338px;width:871px;height:442px;background:#4c5229;padding:8px}
.map{width:100%;height:100%;background:#e8e5dc}

/* faq */
.faq-item{left:209px;width:782px;border:1px solid var(--line);border-radius:4px;background:var(--white)}
.faq-q{height:55px;padding:0 19px;display:flex;align-items:center;justify-content:space-between;font-size:17px;color:var(--text)}
.faq-item.open .faq-q{color:var(--olive-text)}
.faq-a{padding:0 90px 0 21px;font-size:12.5px;line-height:25px;color:var(--text)}
.chev{width:12px;height:12px}

/* footer */
.footer{left:0;top:2338px;width:1200px;height:317px;background:var(--brown-dark)}
.footer-brand{left:160px;top:2376px;width:233px;height:233px;background:var(--brown);box-shadow:0 4px 14px rgba(0,0,0,.35);display:flex;align-items:center;justify-content:center}
.footer-brand .brand-name{font-size:34px}
.footer-head{color:var(--gold);font-size:17px;font-weight:400}
.footer-col{color:var(--white);font-size:15px;line-height:33.5px}
.copyright{right:112px;top:2563px;color:var(--white);font-size:14.5px}
.copyright a{color:var(--gold)}
</style>
</head>
<body>

<section class="abs hero" aria-label="Startbereich"></section>
<div class="abs brand-box"><span class="brand-name">VELURANA</span></div>
<p class="abs tagline tagline-1">Weltneuheit aus Österreich!</p>
<p class="abs tagline tagline-2">Feine Milchschokolade mit dem wertvollen Extrakt von Oliven</p>
<h1 class="abs hero-title"><span class="big">Schokolade statt</span><span class="small">Tabletten.</span></h1>
<div class="abs product" role="img" aria-label="Produktfoto: Schokoladenpackung mit Olivenextrakt und Schokoladenstücke"></div>
<svg class="abs curve" width="1200" height="140" viewBox="0 0 1200 140" aria-hidden="true">
  <path d="M0 0 Q600 238 1200 0 L1200 0 L0 0 Z" fill="#f4f4f4"/>
  <path d="M0 0 Q600 268 1200 0 Q600 238 0 0 Z" fill="#5a2a27"/>
</svg>
<div class="abs dots"><span class="dot active"></span><span class="dot"></span><span class="dot"></span><span class="dot"></span></div>

<p class="abs intro">VELURANA hat die mediterrane Ernährung mit all ihren Vorteilen „komprimiert“ und in eine gesunde Süßigkeit gepackt. Die wichtigste Zutat: Oliven. Aus 240 kg davon gewinnt man 1 kg Oliven-Extrakt, welches von uns in hochwertige Schokolade eingearbeitet wird. Das ist die neue Art der Nahrungsergänzung: konsumiert man täglich drei Mini-Stückchen Schokolade, nimmt man garantiert 5 mg wertvolle, gesundheitsfördernde Polyphenole der Olive zu sich.</p>

<section class="abs finder" aria-label="Apothekenfinder"></section>
<h2 class="abs finder-title">Jetzt VELURANA in der Apotheke gratis testen!</h2>
<div class="abs finder-btn">Postleitzahl eingeben und nächste teilnehmende Apotheke finden</div>
<div class="abs map-frame"><div class="map" role="img" aria-label="Stadtplan mit Standorten teilnehmender Apotheken"></div></div>

<div class="abs faq-item" style="top:1921px">
  <div class="faq-q">Wie ist VELURANA entstanden, wer hat es entwickelt und wer produziert es?<svg class="chev" viewBox="0 0 12 12"><path d="M4 2l4 4-4 4" fill="none" stroke="#555" stroke-width="1.4"/></svg></div>
</div>
<div class="abs faq-item open" style="top:1987px;height:157px">
  <div class="faq-q">Welche Testresultate gibt es zu VELURANA?<svg class="chev" viewBox="0 0 12 12"><path d="M2 4l4 4 4-4" fill="none" stroke="#555" stroke-width="1.4"/></svg></div>
  <p class="faq-a">Sämtliche Entwicklungsstufen wurden sorgfältig zwischen der Manufaktur Bergkamm Schokolade &amp; dem IQLN abgestimmt und laufend seitens des IQLN kontrolliert. Nachstehende Testergebnisse zeigen den Gehalt mindestens 5mg Polyphenolen in der empfohlenen Tagesdosis von 6g (= 1,5 Täfelchen)</p>
</div>
<div class="abs faq-item" style="top:2157px">
  <div class="faq-q">Wie soll VELURANA verwendet werden?<svg class="chev" viewBox="0 0 12 12"><path d="M4 2l4 4-4 4" fill="none" stroke="#555" stroke-width="1.4"/></svg></div>
</div>
<div class="abs faq-item" style="top:2223px">
  <div class="faq-q">Kann man VELURANA auch Kindern geben?<svg class="chev" viewBox="0 0 12 12"><path d="M4 2l4 4-4 4" fill="none" stroke="#555" stroke-width="1.4"/></svg></div>
</div>

<footer class="abs footer"></footer>
<div class="abs footer-brand"><span class="brand-name">VELURANA</span></div>
<h3 class="abs footer-head" style="left:463px;top:2386px">VELURANA – Büro Wien:</h3>
<div class="abs footer-col" style="left:466px;top:2427px">
  <p>Dr. Lukas Hofreiter</p>
  <p>Lindengasse 7/12, A-1070 Wien, Austria,</p>
  <p>office@velurana.at ,</p>
  <p>www.velurana.at.</p>
  <p>Erzeugt in Talheim, Tirol.</p>
</div>
<h3 class="abs footer-head" style="left:849px;top:2386px">KONTAKT</h3>
<div class="abs footer-col" style="left:852px;top:2427px"><p>office@velurana.at</p></div>
<p class="abs copyright">© Copyright 2020.All Rights Reserved.<a href="#">Imprint</a></p>

</body>
</html>
```